Computer tuition business needs Business card and Advertising Flyer

I am starting up a new business "Dorian Featherby Computer Services" (DFCS for short) based in the Manning Valley NSW Australia.
The primary focus is on tuition\advice to the elderly and less computer literate in the region.
I will not be providing any repair services.

I have the line "At your home, On your computer, Answering your questions" in my head

I will need a Business card design (one sided) and Advertising Flyer design (A4 size, grayscale ).

Contact details on all these are - Mobile: 0412-683-904
- Email : dfeatherby.techhelp@examplemail.net

Target Market(s)

The primary focus is on tuition\advice to the elderly and less computer literate in the Manning Valley region of

Industry/Entity Type

Computer

```html
<!DOCTYPE html>
<html lang="en">
<head>
<meta charset="utf-8">
<title>Dorian Featherby Computer Services – Flyer</title>
<link rel="stylesheet" href="https://fonts.googleapis.com/css2?family=Cinzel:wght@700;900&family=Open+Sans:wght@400&family=Archivo+Black&display=swap">
<style>
  :root {
    --ink: #000000;
    --paper: #ffffff;
    --backdrop: #e6e4e0;
  }
  * { margin: 0; padding: 0; box-sizing: border-box; }
  html, body {
    width: 1200px;
    height: 774px;
    overflow: hidden;
    background: var(--backdrop);
  }
  .canvas {
    position: relative;
    width: 1200px;
    height: 774px;
  }
  .flyer {
    position: absolute;
    left: 351px;
    top: 37px;
    width: 497px;
    height: 700px;
    background: var(--paper);
    box-shadow: 0 4px 18px rgba(0, 0, 0, 0.18);
  }
  .flyer__header {
    position: absolute;
    left: 0;
    right: 0;
    top: 10px;
    height: 48px;
    background: var(--ink);
    color: var(--paper);
    display: flex;
    align-items: center;
    justify-content: center;
    font-family: "Cinzel", serif;
    font-weight: 700;
    font-size: 20px;
    letter-spacing: 1.5px;
    white-space: nowrap;
  }
  .brand-name {
    position: absolute;
    left: 0;
    right: 0;
    top: 140px;
    text-align: center;
    font-family: "Open Sans", sans-serif;
    font-weight: 400;
    font-size: 44px;
    letter-spacing: 6px;
    color: var(--ink);
    line-height: 1;
  }
  .headline {
    position: absolute;
    left: 0;
    right: 0;
    top: 268px;
    text-align: center;
    font-family: "Cinzel", serif;
    font-weight: 900;
    font-size: 31px;
    letter-spacing: 1.5px;
    color: var(--ink);
    white-space: nowrap;
  }
  .headline__mark {
    font-family: "Archivo Black", sans-serif;
    font-size: 46px;
    vertical-align: -4px;
  }
  .services {
    position: absolute;
    left: 44px;
    top: 322px;
    list-style: none;
    font-family: "Open Sans", sans-serif;
    font-size: 20px;
    letter-spacing: 0.8px;
    color: var(--ink);
  }
  .services__item {
    display: flex;
    align-items: center;
    height: 49px;
  }
  .services__item::before {
    content: "";
    width: 20px;
    height: 20px;
    border-radius: 50%;
    background: var(--ink);
    margin-right: 14px;
  }
  .call-burst {
    position: absolute;
    left: 118px;
    top: 478px;
    width: 262px;
    height: 196px;
  }
  .call-burst__shape {
    position: absolute;
    inset: 0;
    width: 100%;
    height: 100%;
    filter: drop-shadow(3px 5px 5px rgba(0, 0, 0, 0.35));
  }
  .call-burst__text {
    position: absolute;
    inset: 0;
    display: flex;
    flex-direction: column;
    align-items: center;
    justify-content: center;
    color: var(--paper);
    font-family: "Archivo Black", sans-serif;
    text-align: center;
    line-height: 1.5;
  }
  .call-burst__label { font-size: 18px; letter-spacing: 1px; }
  .call-burst__phone { font-size: 20px; letter-spacing: 1.5px; }
</style>
</head>
<body>
<main class="canvas">
  <article class="flyer">
    <header class="flyer__header">Dorian Featherby Computer Services</header>

    <p class="brand-name">DFCS</p>

    <h1 class="headline">Computer Problems<span class="headline__mark">?</span></h1>

    <ul class="services">
      <li class="services__item">At your home</li>
      <li class="services__item">On your computer</li>
      <li class="services__item">Answering your questions</li>
    </ul>

    <div class="call-burst">
      <svg class="call-burst__shape" viewBox="-105 -105 210 210" preserveAspectRatio="none" aria-hidden="true">
        <polygon fill="#000" points="100,0 76.5,15.2 92.4,38.3 64.8,43.4 70.7,70.7 43.4,64.8 38.3,92.4 15.2,76.5 0,100 -15.2,76.5 -38.3,92.4 -43.4,64.8 -70.7,70.7 -64.8,43.4 -92.4,38.3 -76.5,15.2 -100,0 -76.5,-15.2 -92.4,-38.3 -64.8,-43.4 -70.7,-70.7 -43.4,-64.8 -38.3,-92.4 -15.2,-76.5 0,-100 15.2,-76.5 38.3,-92.4 43.4,-64.8 70.7,-70.7 64.8,-43.4 92.4,-38.3 76.5,-15.2"/>
      </svg>
      <div class="call-burst__text">
        <span class="call-burst__label">Call Now</span>
        <span class="call-burst__phone">0412-683-904</span>
      </div>
    </div>
  </article>
</main>
</body>
</html>
```